Brinevale Yacht Management Full Page Ad Flyer

Yacht Management Package also includes the following periodic Monthly services:

Monthly full vessel systems checklist inspections
Diver For Hull Cleaning And Inspection Of Props, Shafts, and Zincs
Interior/Exterior Detailing and scheduled washdowns
Manage Haulout
Pump-out Services
On-call Captain and Crew Services
Updates

Need more time to provide more content to designers and the printing press template file.

Target Market(s)

Vessel owners, motor yachts, sailboats from 25 feet in length up to 125 feet in length. We do not do cruise ships or yachts larger than 125 feet. Someone who has their boat docked at their house or a local marina. We also offer mobile on-site services.

```html
<!DOCTYPE html>
<html lang="en">
<head>
<meta charset="utf-8">
<title>Brinevale Yacht Management – Flyer</title>
<link href="https://fonts.googleapis.com/css2?family=Exo+2:wght@500;600&family=Russo+One&display=swap" rel="stylesheet">
<style>
  :root {
    --page-bg: #e9eaec;
    --paper: #ffffff;
    --brand-blue: #2b57b3;
    --deep-blue: #1f3f94;
    --sea-dark: #0c5a8c;
    --sea-mid: #1b86b8;
    --sea-light: #2fa9c4;
    --badge-grey: #9a9a9a;
    --arc-grey: #8a8a8a;
    --ink: #1c1c1c;
    --white: #ffffff;
  }
  * { margin: 0; padding: 0; box-sizing: border-box; }
  html, body {
    width: 1200px; height: 998px; overflow: hidden;
    background: var(--page-bg);
  }
  .flyer {
    position: absolute; left: 258px; top: 19px;
    width: 684px; height: 960px;
    background: var(--paper);
    overflow: hidden;
    box-shadow: 0 4px 18px rgba(0,0,0,.18);
  }
  .flyer-shapes { position: absolute; inset: 0; width: 100%; height: 100%; }
  .brand-name {
    position: absolute; left: 37px; top: 44px;
    font: 500 25px/1 "Exo 2", sans-serif;
    letter-spacing: 4px;
    color: var(--deep-blue);
    text-transform: uppercase;
  }
  .headline {
    position: absolute; left: 38px; top: 168px;
    font: 400 53px/52px "Russo One", sans-serif;
    letter-spacing: 1.5px;
    color: var(--white);
    text-transform: uppercase;
  }
  .service-list {
    position: absolute; left: 86px; top: 591px; width: 500px;
    list-style: none;
    font: 500 19.5px/22px "Exo 2", sans-serif;
    color: var(--ink);
  }
  .service-list li {
    position: relative; padding-left: 25px; margin-bottom: 19px;
  }
  .service-list li svg {
    position: absolute; left: 0; top: 5px; width: 13px; height: 13px;
  }
  .size-badge {
    position: absolute; left: 382px; top: 780px; width: 270px;
    text-align: center;
    font: 400 27px/28px "Russo One", sans-serif;
    color: var(--white);
    text-transform: uppercase;
  }
  .web-address {
    position: absolute; left: 376px; top: 929px;
    font: 600 14.5px/1 "Exo 2", sans-serif;
    letter-spacing: .4px;
    color: var(--white);
  }
</style>
</head>
<body>
  <main class="flyer">
    <svg class="flyer-shapes" viewBox="0 0 684 960">
      <defs>
        <linearGradient id="sea" x1="0" y1="0" x2="1" y2="1">
          <stop offset="0" stop-color="var(--sea-light)"/>
          <stop offset=".5" stop-color="var(--sea-mid)"/>
          <stop offset="1" stop-color="var(--sea-dark)"/>
        </linearGradient>
        <radialGradient id="badge" cx=".5" cy=".35" r=".7">
          <stop offset="0" stop-color="#b4b4b4"/>
          <stop offset="1" stop-color="var(--badge-grey)"/>
        </radialGradient>
      </defs>
      <path role="img" aria-label="Aerial photo of a white motor yacht on clear turquoise sea"
            d="M0 170 C180 90 420 45 684 30 L684 410 C520 440 250 480 0 548 Z"
            fill="url(#sea)"/>
      <path d="M330 128 C420 95 500 70 520 48 C470 72 400 92 330 128 Z" fill="var(--paper)"/>
      <path d="M0 548 C250 480 520 440 684 410 L684 442 C600 448 520 470 500 500 C510 545 470 560 400 572 C520 520 480 480 380 490 C230 505 110 528 0 560 Z"
            fill="var(--brand-blue)"/>
      <path d="M80 570 C35 680 30 850 56 960 L44 960 C18 850 28 690 80 570 Z" fill="var(--arc-grey)"/>
      <circle cx="517" cy="875" r="130" fill="url(#badge)"/>
      <path d="M170 960 C330 920 520 905 684 905 L684 960 Z" fill="var(--brand-blue)"/>
    </svg>

    <div class="brand-name">Brinevale</div>

    <h1 class="headline">Yacht<br>Management<br>Package</h1>

    <ul class="service-list">
      <li><svg viewBox="0 0 13 13"><circle cx="6.5" cy="6.5" r="6.5" fill="var(--brand-blue)"/><path d="M3.5 6.7l2 2 4-4" stroke="#fff" stroke-width="1.7" fill="none"/></svg>Monthly full vessel systems checklist inspections</li>
      <li><svg viewBox="0 0 13 13"><circle cx="6.5" cy="6.5" r="6.5" fill="var(--brand-blue)"/><path d="M3.5 6.7l2 2 4-4" stroke="#fff" stroke-width="1.7" fill="none"/></svg>Diver For Hull Cleaning And Inspection Of Props,<br>Shafts, and Zincs</li>
      <li><svg viewBox="0 0 13 13"><circle cx="6.5" cy="6.5" r="6.5" fill="var(--brand-blue)"/><path d="M3.5 6.7l2 2 4-4" stroke="#fff" stroke-width="1.7" fill="none"/></svg>Interior/Exterior Detailing and scheduled washdowns</li>
      <li><svg viewBox="0 0 13 13"><circle cx="6.5" cy="6.5" r="6.5" fill="var(--brand-blue)"/><path d="M3.5 6.7l2 2 4-4" stroke="#fff" stroke-width="1.7" fill="none"/></svg>Manage Haulout</li>
      <li><svg viewBox="0 0 13 13"><circle cx="6.5" cy="6.5" r="6.5" fill="var(--brand-blue)"/><path d="M3.5 6.7l2 2 4-4" stroke="#fff" stroke-width="1.7" fill="none"/></svg>Pump-out Services</li>
      <li><svg viewBox="0 0 13 13"><circle cx="6.5" cy="6.5" r="6.5" fill="var(--brand-blue)"/><path d="M3.5 6.7l2 2 4-4" stroke="#fff" stroke-width="1.7" fill="none"/></svg>On-call Captain and Crew<br>Services</li>
    </ul>

    <p class="size-badge">25 Feet<br>In Length<br>Up To125 Feet<br>In Length</p>

    <p class="web-address">www.brinevaleyachtmanagement.com</p>
  </main>
</body>
</html>
```